Fall Convention Graphic Designs (logo, digital brochure, t-shirt designs, social media templates)

I need a graphic package for the Brightwell Dance Guild Fall Dance Convention. Brightwell Dance Guild is a non-profit organization of dance teachers, and this educational dance conference is for members and their students with multiple events throughout the weekend. The convention has a new them each year. I will need a package with a general "logo" type graphic, a digital brochure, t-shirt design, and social media graphic templates. This year's Convention has a general theme and names for each event throughout the weekend.
The theme and event names for this year are:
Convention Theme Tales in Motion: Beneath a Silver Sky
Registration Desk The Willow Nook
Members Welcome A Golden Greeting
Banquet A Velvet Soiree
President's Reception Glow Beyond Dusk
Jr. Member Desk Wanderers' Wharf
Jr. Member Pizza Party Meadow Mixer
Members Luncheon Harbor Reveries

I am attaching a word file that includes information and text to be included in brochure. Also attached are designs from previous years for brochures, T-shirts, and social media graphics.

Colors that we will be using for decorations at various events over the weekend this year are shades of green (fern and mossy green), shades of blue (including navy), white, and pinks (including mauve). The banquet event will be decorated as an enchanted forest. We are using fairy lights, books that look like a storybook, and lanterns for decorations as well. I think I would like a more modern design, and I do not want anything that is childish or too whimsical. While we are using floral decorations I don't want bunches of flowers in the design.

*I am open to seeing initial logo type designs and giving feedback to make sure it is a direction that I like and then moving forward with the other parts of the project.

```html
<!DOCTYPE html>
<html lang="en">
<head>
<meta charset="utf-8">
<title>Brightwell Dance Guild Fall Convention – Initial Proposal</title>
<link rel="stylesheet" href="https://fonts.googleapis.com/css2?family=Fredoka:wght@600;700&family=Poppins:wght@400;700&family=Open+Sans:wght@400;600;700&display=swap">
<style>
  :root {
    --board: #666666;
    --ink-light: #ffffff;
    --frame: #bdbdbd;
    --night: #000000;
    --teal: #17968f;
    --teal-bright: #2fd6c4;
    --aurora-blue: #1d5fbf;
    --moss: #9ab547;
    --moss-deep: #6d8a2c;
  }
  * { box-sizing: border-box; margin: 0; padding: 0; }
  html, body { width: 1200px; height: 930px; overflow: hidden; }
  body { background: var(--board); position: relative; font-family: "Open Sans", sans-serif; color: var(--ink-light); }

  .proposal-note {
    position: absolute; left: 138px; top: 45px; width: 735px; height: 81px;
    border: 1px solid var(--frame); padding: 13px 15px;
    font-family: "Poppins", sans-serif;
  }
  .proposal-note__label { font-weight: 700; font-size: 15px; color: #e8e8e8; letter-spacing: .2px; }
  .proposal-note__text { margin-top: 8px; font-size: 16.5px; font-weight: 400; color: #ececec; }

  /* Brochure cover */
  .cover {
    position: absolute; left: 134px; top: 165px; width: 521px; height: 695px; overflow: hidden;
  }
  .cover__art {
    position: absolute; inset: 0;
    background:
      linear-gradient(180deg, var(--night) 0%, var(--night) 38%, #06213a 48%, var(--aurora-blue) 60%, var(--teal-bright) 72%, #7fc95a 84%, var(--moss) 100%);
  }
  .cover__art::after {
    content: ""; position: absolute; left: 40px; right: 40px; top: 370px; bottom: 0;
    background: radial-gradient(ellipse at 50% 55%, rgba(0,0,0,.92) 0%, rgba(0,0,0,.85) 45%, rgba(0,0,0,0) 72%);
  }
  .cover__org {
    position: absolute; top: 24px; left: 0; right: 0; text-align: center;
    font-weight: 600; font-size: 16px; line-height: 19px; letter-spacing: .3px;
  }
  .cover__org-rule { display: flex; align-items: center; justify-content: center; gap: 7px; }
  .cover__org-rule::before, .cover__org-rule::after {
    content: ""; height: 1px; width: 135px;
  }
  .cover__org-rule::before { background: linear-gradient(90deg, transparent, #fff); }
  .cover__org-rule::after { background: linear-gradient(90deg, #fff, transparent); }

  .title { position: absolute; font-family: "Fredoka", sans-serif; font-weight: 700; color: var(--ink-light); white-space: nowrap; line-height: 1; }
  .title--shadow { text-shadow: 2px 2px 0 var(--teal); }
  .title-rule { position: absolute; height: 2px; background: #fff; box-shadow: 1px 1px 0 var(--teal); }

  .cover__detail {
    position: absolute; top: 589px; text-align: center; font-weight: 600; font-size: 14px; line-height: 15px;
    text-shadow: 0 1px 3px rgba(0,0,0,.5);
  }
  .cover__detail--date { left: 20px; width: 220px; }
  .cover__detail--venue { left: 282px; width: 220px; letter-spacing: .6px; }

  /* Round badge */
  .badge { position: absolute; left: 717px; top: 338px; width: 350px; height: 350px; }
  .badge__art {
    position: absolute; inset: 0; border-radius: 50%;
    background: linear-gradient(180deg, var(--night) 0%, var(--night) 62%, #0b2b55 74%, var(--aurora-blue) 84%, var(--teal-bright) 93%, var(--moss) 100%);
  }
  .badge__ring { position: absolute; inset: 0; }
</style>
</head>
<body>

<section class="proposal-note">
  <p class="proposal-note__label">INITIAL PROPOSAL<span style="font-weight:400">:</span></p>
  <p class="proposal-note__text">for the graphic package for the Brightwell Dance Guild Autumn Dance Convention.</p>
</section>

<article class="cover">
  <div class="cover__art" role="img" aria-label="Starry night sky with teal aurora over a silhouetted oak tree, hills and spreading roots on mossy green ground"></div>

  <header class="cover__org">
    <p>BRIGHTWELL DANCE GUILD, INC.</p>
    <p class="cover__org-rule">FALL CONVENTION</p>
  </header>

  <span class="title-rule" style="left:42px; top:154px; width:36px; transform:rotate(-4deg);"></span>
  <h1>
    <span class="title title--shadow" style="left:84px; top:128px; font-size:25px; transform:rotate(-4deg); transform-origin:left bottom;">Tales in Motion:</span>
    <span class="title title--shadow" style="left:42px; top:168px; font-size:44px; transform:rotate(-3deg); transform-origin:left bottom; text-shadow:3px 3px 0 var(--teal);">Beneath a</span>
    <span class="title title--shadow" style="left:54px; top:218px; font-size:84px; transform:rotate(-3deg); transform-origin:left bottom; text-shadow:4px 4px 0 var(--teal);">Silver</span>
    <span class="title title--shadow" style="left:270px; top:272px; font-size:76px; transform:rotate(-3deg); transform-origin:left bottom; text-shadow:4px 4px 0 var(--teal);">Sky</span>
  </h1>
  <span class="title-rule" style="left:282px; top:177px; width:112px; transform:rotate(-3deg);"></span>
  <span class="title-rule" style="left:64px; top:323px; width:190px; transform:rotate(-3deg);"></span>

  <p class="cover__detail cover__detail--date">November 19 – 22, 2026<br>Linden Hall Convention Center</p>
  <p class="cover__detail cover__detail--venue">Harborview Grand Hotel<br>Ashbury, NC</p>
</article>

<article class="badge">
  <div class="badge__art" role="img" aria-label="Round night sky badge with stars and a teal aurora glowing along the lower edge"></div>
  <svg class="badge__ring" viewBox="0 0 350 350" width="350" height="350">
    <defs>
      <path id="outer-arc" d="M 20 160 A 155 155 0 0 1 330 160"/>
      <path id="inner-arc" d="M 36 165 A 139 139 0 0 1 314 165"/>
    </defs>
    <text font-family="Open Sans, sans-serif" font-weight="700" font-size="15.5" fill="#ffffff" letter-spacing="0.8">
      <textPath href="#outer-arc" startOffset="0">• BRIGHTWELL DANCE GUILD, INC. • FALL CONVENTION</textPath>
    </text>
    <text font-family="Open Sans, sans-serif" font-weight="400" font-size="8.2" fill="#ffffff">
      <textPath href="#inner-arc" startOffset="2">November 19 – 22, 2026, Linden Hall Convention Center · Harborview Grand Hotel, Ashbury, NC</textPath>
    </text>
  </svg>
  <span class="title-rule" style="left:50px; top:137px; width:22px; transform:rotate(-3deg); height:1.5px;"></span>
  <span class="title title--shadow" style="left:76px; top:120px; font-size:15px; transform:rotate(-3deg); text-shadow:1px 1px 0 var(--teal);">Tales in Motion:</span>
  <span class="title title--shadow" style="left:48px; top:140px; font-size:25px; transform:rotate(-2deg); text-shadow:2px 2px 0 var(--teal);">Beneath a</span>
  <span class="title-rule" style="left:188px; top:151px; width:68px; transform:rotate(-2deg); height:1.5px;"></span>
  <span class="title title--shadow" style="left:56px; top:168px; font-size:47px; transform:rotate(-2deg); text-shadow:2px 2px 0 var(--teal);">Silver</span>
  <span class="title title--shadow" style="left:188px; top:204px; font-size:42px; transform:rotate(-2deg); text-shadow:2px 2px 0 var(--teal);">Sky</span>
  <span class="title-rule" style="left:62px; top:240px; width:120px; transform:rotate(-2deg); height:1.5px;"></span>
</article>

</body>
</html>
```